Innovative approaches to treat addiction

PowerPoint on different techniques
Add graphics to screen
Easy to follow
I've provided the PowerPoint w content
Now make it pretty
And
hand outs for them to follow and take notes
Can you also add my bio:
Mara J. Thornquist, MS LCADC is a licensed Psychotherapist with a specialty in Addiction Disorders and over 22 years of clinical experience. Her integrative approach to counseling combines years of clinical experience with cognitive behavioral and traditional psychotherapy, with holistic therapies including; mindfulness, NLP, hypnotherapy, yoga therapy, reiki, motivational and wellness coaching.
Handout materials for them to follow and take notes

```html
<!DOCTYPE html>
<html lang="en">
<head>
<meta charset="utf-8">
<title>Innovative Approaches to Treat Addiction – Handout</title>
<link href="https://fonts.googleapis.com/css2?family=Questrial&family=Roboto:wght@400;500&display=swap" rel="stylesheet">
<style>
  :root{
    --backdrop:#e9e4df;
    --paper:#ffffff;
    --ink:#1d1d1d;
    --slide-ink:#3a3a3a;
    --purple-dark:#3b1247;
    --purple:#5e2470;
    --purple-light:#7b3b8c;
    --magenta:#a8186a;
    --name-pink:#e0449a;
    --rule:#2b2b2b;
    --frame:#2a2a2a;
  }
  *{box-sizing:border-box;margin:0;padding:0}
  html,body{width:1200px;height:850px;overflow:hidden}
  body{background:var(--backdrop);position:relative;font-family:"Questrial",sans-serif;color:var(--ink)}
  .page{position:absolute;top:58px;width:520px;height:736px;background:var(--paper);box-shadow:0 2px 10px rgba(0,0,0,.18)}
  .page--left{left:52px}
  .page--right{left:628px}
  .page__date{position:absolute;right:6px;top:4px;font-family:"Roboto",sans-serif;font-size:10.5px}
  .page__number{position:absolute;right:8px;bottom:20px;font-family:"Roboto",sans-serif;font-size:9.5px}

  .handout-row{position:absolute;left:36px;width:450px;height:160px}
  .slide{position:absolute;left:0;top:0;width:214px;height:159px;border:1px solid var(--frame);background:var(--paper);overflow:hidden}
  .slide__band{position:absolute;left:12px;top:12px;width:190px;height:34px;
    background:linear-gradient(100deg,var(--purple-dark),var(--purple) 55%,var(--purple-light));
    clip-path:polygon(0 0,100% 0,100% 82%,50% 100%,0 82%);
    color:#fff;font-size:9.3px;padding:0 10px;display:flex;align-items:center;line-height:1.15}
  .slide__tab{position:absolute;left:182px;top:0;width:14px;height:24px;background:var(--magenta)}
  .slide__body{position:absolute;left:22px;top:60px;width:145px;font-family:"Roboto",sans-serif;font-size:3.3px;line-height:1.28;color:var(--slide-ink)}
  .slide__body--wide{width:172px;top:54px}
  .slide__body p{position:relative;padding-left:6px;margin-bottom:2.2px}
  .slide__body p::before{content:"";position:absolute;left:0;top:.6px;border-left:2.4px solid var(--magenta);border-top:1.3px solid transparent;border-bottom:1.3px solid transparent}
  .slide__body p.sub{margin-left:6px}
  .slide__body p.label{font-size:4.4px}
  .slide__body p.ref{padding-left:0;font-weight:500;margin-top:3px}
  .slide__body p.ref::before{display:none}
  .slide__art{position:absolute}

  .notes{position:absolute;left:256px;top:22px;width:214px}
  .notes span{display:block;height:22.8px;border-bottom:1px solid var(--rule)}
  .notes span:first-child{height:1px}

  .bio{position:absolute;left:74px;top:500px;width:376px;height:172px;
    background:linear-gradient(120deg,#4a1858,var(--purple) 50%,#6c2d80);color:#fff}
  .bio__text{position:absolute;left:13px;top:14px;width:256px;font-size:9.8px;line-height:12.2px;text-align:justify}
  .bio__name{color:var(--name-pink);font-weight:bold;letter-spacing:.4px}
  .bio__photo{position:absolute;left:278px;top:10px;width:88px;height:112px;border-radius:8px;
    background:linear-gradient(170deg,#d8d2d0,#8a6a60 60%,#3a2a2a)}
  .bio__phone{position:absolute;left:13px;top:136px;width:126px;height:26px;background:#fff;display:flex;align-items:center;gap:8px;padding-left:5px;
    color:var(--purple);font-size:14px}
</style>
</head>
<body>

<section class="page page--left">
  <div class="page__date">20.10.2016</div>

  <div class="handout-row" style="top:74px">
    <div class="slide">
      <div class="slide__tab"></div>
      <div class="slide__band">Yoga Asana/ Hand Mudra</div>
      <div class="slide__body">
        <p>Physical postures of yoga replace negative thinking with calm, focused movement.</p>
        <p>Hand mudras are postures of the body, in most cases the hand, that shift mood.</p>
        <p class="label">Benefits:</p>
        <p class="sub">Helps clients integrate mindful breathing and body awareness for steadier overall wellbeing.</p>
        <p class="label">Research:</p>
        <p class="sub">Studies of regular practice report lower stress, better sleep and stronger emotional regulation in recovery.</p>
        <p class="sub ref">Author, A. (2016). Yoga and the heart. Retrieved August 2016.</p>
      </div>
      <div class="slide__art" role="img" aria-label="Photo of a person meditating in a yoga pose" style="left:170px;top:58px;width:38px;height:48px;background:linear-gradient(180deg,#cfe3ef,#6c9fbf 60%,#3d5e7a)"></div>
    </div>
    <div class="notes"><span></span><span></span><span></span><span></span><span></span><span></span><span></span><span></span></div>
  </div>

  <div class="handout-row" style="top:288px">
    <div class="slide">
      <div class="slide__tab"></div>
      <div class="slide__band">Hypnosis/ Self Hypnosis</div>
      <div class="slide__body">
        <p>The practice of creating new healthy patterns through deep relaxed concentration and self-care.</p>
        <p class="label">Benefits:</p>
        <p class="sub">Improves immune function, self-control, relaxation and reduces relapse risk.</p>
        <p class="label">Research:</p>
        <p class="sub">Clinical programs report reduced pain, nausea and recovery time among patients using guided hypnosis sessions.</p>
        <p class="sub ref">Author, B. (2015). The science of breathing. Retrieved July 2016.</p>
      </div>
      <div class="slide__art" role="img" aria-label="Illustration of a glowing head in a calm trance" style="left:170px;top:64px;width:40px;height:46px;border-radius:50%;background:radial-gradient(circle,#e6eefa,#8aa3cf 60%,#3b4f86)"></div>
    </div>
    <div class="notes"><span></span><span></span><span></span><span></span><span></span><span></span><span></span><span></span></div>
  </div>

  <div class="handout-row" style="top:501px">
    <div class="slide">
      <div class="slide__tab"></div>
      <div class="slide__band">Neuro-linguistic Programming (NLP)</div>
      <div class="slide__body">
        <p>NLP is a set of tools that reshape behaviors and thoughts from a linguistic perspective.</p>
        <p class="label">Benefits:</p>
        <p class="sub">Builds rapport, empowers the individual, fast repeatable outcomes.</p>
        <p class="label">Research:</p>
        <p class="sub">Studies found awareness of sensory systems effective in reducing emotional responses.</p>
        <p class="sub ref">Changing behaviour with NLP. Retrieved August 2016.</p>
      </div>
      <div class="slide__art" role="img" aria-label="Illustration of a head profile with a glowing brain network" style="left:168px;top:66px;width:42px;height:46px;border-radius:50% 50% 40% 40%;background:radial-gradient(circle at 60% 40%,#7aa6e6,#223c8a 60%,#0e1a40)"></div>
    </div>
    <div class="notes"><span></span><span></span><span></span><span></span><span></span><span></span><span></span><span></span></div>
  </div>

  <div class="page__number">3</div>
</section>

<section class="page page--right">
  <div class="page__date">20.10.2016</div>

  <div class="handout-row" style="top:74px">
    <div class="slide">
      <div class="slide__tab"></div>
      <div class="slide__band">Progressive Muscles Relaxation and Guided Imagery</div>
      <div class="slide__body">
        <p>Guided imagery is a powerful tool that directs the imagination toward calm.</p>
        <p>Progressive muscle relaxation helps release tension from the body.</p>
        <p class="label">Benefits:</p>
        <p class="sub">Relieves stress and can be used alone or with a guide.</p>
        <p class="label">Research:</p>
        <p class="sub">Reviews link regular relaxation practice with lower anxiety and improved sleep.</p>
        <p class="sub ref">Author, C. (2015). Muscle relaxation to minimize stress.</p>
      </div>
      <div class="slide__art" role="img" aria-label="Illustration of a meditating figure with glowing energy centers" style="left:180px;top:62px;width:28px;height:48px;background:linear-gradient(180deg,#7a4bd0,#2d6fd8 40%,#1a1f5a)"></div>
    </div>
    <div class="notes"><span></span><span></span><span></span><span></span><span></span><span></span><span></span><span></span></div>
  </div>

  <div class="handout-row" style="top:288px">
    <div class="slide">
      <div class="slide__tab"></div>
      <div class="slide__band">Sources</div>
      <div class="slide__body slide__body--wide">
        <p>Author, C. (2015). Using progressive muscle relaxation to minimize stress. Retrieved August 2016.</p>
        <p>Author, D. (2014). Breathing practices for treatment of stress related conditions.</p>
        <p>Author, E. (2013). Hypnotherapy and recovery. Retrieved July 2016.</p>
        <p>Author, F. (2011). Hypnosis today. Retrieved July 2016.</p>
        <p>Author, G. (2014). Mindfulness based relapse prevention in substance use disorders: a randomized trial.</p>
        <p>Author, H. (2015). Compassion meditation reduces mind wandering. Retrieved July 2016.</p>
        <p>Author, B. (2015). The science of breathing. Retrieved July 2016.</p>
        <p>Author, I. (2016). Changing behaviour with neuro-linguistic programming. Retrieved July 2016.</p>
        <p>Author, A. (2016). Yoga and the heart. Retrieved August 2016.</p>
        <p>Author, J. (2016). What is guided imagery? Retrieved August 2016.</p>
      </div>
    </div>
    <div class="notes"><span></span><span></span><span></span><span></span><span></span><span></span><span></span><span></span></div>
  </div>

  <div class="bio">
    <p class="bio__text"><span class="bio__name">Mara J. Thornquist</span>, MS LCADC is a licensed Psychotherapist with a specialty in Addiction Disorders and over 22 years of clinical experience. Her integrative approach to counseling combines years of clinical experience with cognitive behavioral and traditional psychotherapy, with holistic therapies including; mindfulness, NLP, hypnotherapy, yoga therapy, reiki, motivational and wellness coaching.</p>
    <div class="bio__photo" role="img" aria-label="Portrait photo of the therapist"></div>
    <div class="bio__phone">
      <svg width="20" height="20" viewBox="0 0 20 20" aria-hidden="true">
        <circle cx="10" cy="10" r="10" fill="#6a2a7e"/>
        <path d="M7 5.2c.4-.3.9-.2 1.1.2l1 1.8c.2.4.1.8-.2 1.1l-.6.5c.5 1.1 1.3 2 2.4 2.5l.5-.6c.3-.3.7-.4 1.1-.2l1.8 1c.4.2.5.7.2 1.1l-.7.9c-.4.5-1.1.7-1.7.4-2.6-1-4.6-3-5.6-5.6-.2-.6 0-1.3.5-1.700z" fill="#fff"/>
      </svg>
      <span>410-555-0172</span>
    </div>
  </div>

  <div class="page__number">4</div>
</section>

</body>
</html>
```